TMVG Website

Hi we require a website with similar attributes and design to this http://layout7.fernquaysites.com but obviously with all our information and images etc... also attached are our logos please do the design with the yellow logo not the red.

```html
<!DOCTYPE html>
<html lang="en">
<head>
<meta charset="utf-8">
<title>Tarmvale Collision Repair Centre</title>
<link rel="stylesheet" href="https://fonts.googleapis.com/css2?family=Lato:wght@400;700&family=Montserrat:wght@400;500&family=Oswald:wght@500;600&display=swap">
<style>
:root{
  --black:#000;
  --gold:#e8d21a;
  --yellow:#f6e21c;
  --green-line:#1f9a4a;
  --text:#ffffff;
}
*{box-sizing:border-box;margin:0;padding:0}
html,body{width:784px;height:1200px;overflow:hidden;background:var(--black)}
body{position:relative;font-family:"Lato",sans-serif;color:var(--text)}
.abs{position:absolute}

/* header */
.site-header{left:0;top:0;width:784px;height:190px;
  background:radial-gradient(ellipse at 50% 20%,#2a2a2a 0%,#0c0c0c 55%,#000 100%)}
.brand{left:292px;top:58px;width:200px;text-align:center}
.brand-mark{display:flex;align-items:center;justify-content:center;gap:8px;
  font-weight:700;font-size:30px;color:var(--gold);letter-spacing:2px}
.brand-mark .dot{width:12px;height:12px;background:var(--gold)}
.brand-name{font-weight:700;font-size:13px;color:var(--gold);margin-top:4px;letter-spacing:.5px}
.brand-sub{font-weight:700;font-size:9px;color:var(--gold);letter-spacing:1px}
.nav-band{left:130px;top:134px;width:530px;height:50px}
.main-nav{left:0;top:156px;width:784px;display:flex;justify-content:center;gap:14px;
  font-family:"Montserrat",sans-serif;font-size:11.5px;color:var(--text)}
.main-nav a{color:inherit;text-decoration:none}
.main-nav a:last-child{margin-left:6px}

/* hero */
.hero-photo{left:130px;top:200px;width:520px;height:210px;
  background:radial-gradient(ellipse at 55% 55%,#3a3344 0%,#1c1822 45%,#000 80%)}
.hero-rule{left:85px;top:467px;width:575px;height:3px;
  background:linear-gradient(90deg,#c7a20e,#e8c21a 60%,#7a5a08)}

/* main */
.main{left:0;top:472px;width:784px;height:430px;
  background:repeating-linear-gradient(90deg,#0b0b0b 0 2px,#141414 2px 3px,#080808 3px 5px)}
.welcome-kicker{left:88px;top:512px;font-size:9.5px;letter-spacing:.3px}
.welcome-title{left:88px;top:535px;font-size:11px;font-weight:700;color:var(--gold)}
.welcome-copy{left:88px;top:553px;width:404px;font-size:7.9px;line-height:19.6px;color:var(--text)}
.badge{left:90px;top:690px;width:112px;height:148px;display:flex;align-items:center;gap:6px;
  font-weight:700;font-size:13px;color:var(--gold)}
.badge .dot{width:10px;height:10px;background:var(--gold);flex:none}

.side-head{left:506px;width:192px;height:34px}
.side-head span{position:absolute;left:16px;top:11px;font-family:"Oswald",sans-serif;font-weight:600;
  font-size:11px;color:#fff;letter-spacing:.3px}
.service-card{left:506px;top:550px;width:197px;height:122px;
  background:linear-gradient(180deg,#6f7a6a 0%,#8a8c3c 30%,#bfb62a 60%,#9a9420 100%)}
.service-card h3{position:absolute;left:8px;top:42px;font-family:"Oswald",sans-serif;font-weight:600;font-size:11px;color:#fff}
.service-card p{position:absolute;left:8px;top:61px;width:183px;font-size:7.4px;line-height:11.2px;color:#fff;text-align:justify}
.service-card a{position:absolute;left:8px;top:107px;font-size:7.6px;font-weight:700;color:#fff;text-decoration:none}

.contact-form{left:507px;top:733px;width:189px;height:153px;
  background:linear-gradient(180deg,var(--yellow) 0%,#eedd2a 60%,#d9d07a 100%)}
.contact-form label{position:absolute;font-size:7.4px;font-weight:700;color:#2b2700}
.contact-form .field{position:absolute;background:#fff;height:19px;font-size:7.4px;color:#888;padding:6px 8px}

/* strip */
.service-list{left:85px;top:916px;width:187px;height:83px;
  background:linear-gradient(160deg,#8a8624,#5b5a18);padding:9px 12px;font-size:8.6px;line-height:14px;color:#fff;list-style:none}
.estimate-box{left:299px;top:916px;width:184px;height:84px;
  background:radial-gradient(ellipse at 60% 80%,#5b6a16,#2f3a10 70%)}
.estimate-btn{left:313px;top:930px;width:151px;height:25px;background:#fff;color:#222;
  font-size:9.6px;display:flex;align-items:center;justify-content:center}
.coupon{left:512px;top:916px;width:186px;height:80px}
.coupon-text{left:542px;top:924px;width:150px;font-size:8px;line-height:11.2px;color:#fff}
.coupon-text strong{display:block;font-size:8.6px;font-weight:400;margin-bottom:7px}

/* footer */
.footer-rule{left:83px;top:1030px;width:615px;height:5px;
  background:linear-gradient(180deg,#0f3a1c 0%,var(--green-line) 50%,#8a9a20 100%)}
.footer-car{left:380px;top:1100px;width:404px;height:100px;
  background:radial-gradient(ellipse at 60% 70%,#1e1e22,#000 70%)}
.social{left:88px;top:1046px;display:flex;gap:6px;align-items:center}
.social .ring{width:8px;height:8px;border-radius:50%;background:#fff}
.footer-name{left:85px;top:1078px;font-family:"Montserrat",sans-serif;font-weight:500;font-size:10.4px}
.footer-lines{left:85px;top:1120px;font-size:7.4px;line-height:19.6px;color:#fff}
</style>
</head>
<body>

<header class="site-header abs" role="img" aria-label="Dark textured header backdrop"></header>
<div class="brand abs">
  <div class="brand-mark"><span class="dot"></span>TMVG</div>
  <div class="brand-name">TARMVALE COLLISION</div>
  <div class="brand-sub">REPAIR CENTRE</div>
</div>
<svg class="nav-band abs" viewBox="0 0 530 50" aria-hidden="true">
  <defs>
    <linearGradient id="bandFill" x1="0" y1="0" x2="0" y2="1">
      <stop offset="0" stop-color="#b8a80a"/>
      <stop offset=".5" stop-color="#e8d21a"/>
      <stop offset="1" stop-color="#4a4406"/>
    </linearGradient>
  </defs>
  <path d="M2 6 Q265 20 528 4 L510 46 Q265 36 20 46 Z" fill="url(#bandFill)"/>
  <path d="M2 6 Q265 20 528 4" fill="none" stroke="#f5ea60" stroke-width="2"/>
</svg>
<nav class="main-nav abs">
  <a href="#">Online Estimate</a><a href="#">Services</a><a href="#">Contact Us</a>
</nav>

<div class="hero-photo abs" role="img" aria-label="Black sports car seen from the rear with amber tail lights on a dark background"></div>
<div class="hero-rule abs"></div>

<section class="main abs"></section>
<p class="welcome-kicker abs">WELCOME</p>
<h1 class="welcome-title abs">Tarmvale Collision</h1>
<p class="welcome-copy abs">We're excited to launch our new website! Please feel free to leave comments and suggestions. We are continually striving to improve our service and we welcome your input. At Layout 7, we make customer service a priority. Our people are highly trained and are dedicated to the commitment of quality, workmanship and service that our business was in fact, founded on. Our technicians have several years of experience behind them. We're proud to serve the auto body repair needs of the Corvale area. When the safety of your family is on the line, why settle for second best.</p>
<div class="badge abs"><span class="dot"></span>Tarmvale</div>

<svg class="side-head abs" style="top:502px" viewBox="0 0 192 34" aria-hidden="true">
  <path d="M0 0 H192 L186 32 H0 Z" fill="#2f5a2a"/>
  <path d="M0 4 H180 L176 34 H0 Z" fill="#e0d21e"/>
  <path d="M182 2 H192 L186 32 H178 Z" fill="#f2f2f2"/>
</svg>
<div class="side-head abs" style="top:502px"><span>SERVICES</span></div>

<div class="service-card abs" role="img" aria-label="Technician working on a car in an auto body workshop">
  <h3>AUTO BODY REPAIR</h3>
  <p>Lorem Ipsum is simply dummy text of the printing and typesetting industry.Lorem Ipsum is simply dummy text of the printing and typesetting industry.</p>
  <a href="#">LERN MORE DETAILS</a>
</div>

<svg class="side-head abs" style="top:688px" viewBox="0 0 192 34" aria-hidden="true">
  <path d="M0 0 H192 L186 32 H0 Z" fill="#2f5a2a"/>
  <path d="M0 4 H180 L176 34 H0 Z" fill="#e0d21e"/>
  <path d="M182 2 H192 L186 32 H178 Z" fill="#f2f2f2"/>
</svg>
<div class="side-head abs" style="top:688px"><span>CONTACT FORM</span></div>

<form class="contact-form abs">
  <label style="left:8px;top:9px">NAME *</label>
  <div class="field" style="left:7px;top:22px;width:82px">First Name</div>
  <div class="field" style="left:97px;top:22px;width:82px">Last Name</div>
  <label style="left:8px;top:49px">E-MAIL *</label>
  <label style="left:98px;top:49px">PHONE *</label>
  <div class="field" style="left:7px;top:61px;width:82px">E-mail Address</div>
  <div class="field" style="left:97px;top:61px;width:82px">Phone Number</div>
  <label style="left:8px;top:88px">TELL US WHAT'S ON YOUR MIND</label>
  <div class="field" style="left:7px;top:100px;width:172px;height:41px">Tell Us What's On Your Mind</div>
</form>

<ul class="service-list abs">
  <li>Auto Body Repair</li>
  <li>Paintless Dent Repair</li>
  <li>Towing</li>
  <li>Auto Body Refinishing</li>
  <li>Automotive Detailing &amp; More</li>
</ul>
<div class="estimate-box abs"></div>
<svg class="abs" style="left:470px;top:988px" width="14" height="13" aria-hidden="true"><path d="M0 13 L14 0 V13 Z" fill="#000"/></svg>
<a class="estimate-btn abs">GET AN ONLINE ASTIMATE</a>

<svg class="coupon abs" viewBox="0 0 186 80" aria-hidden="true">
  <defs>
    <linearGradient id="couponFill" x1="0" y1="0" x2="1" y2="1">
      <stop offset="0" stop-color="#8a8a20"/><stop offset="1" stop-color="#b9b430"/>
    </linearGradient>
  </defs>
  <path d="M8 0 H178 Q178 8 186 8 V72 Q178 72 178 80 H8 Q8 72 0 72 V8 Q8 8 8 0 Z" fill="url(#couponFill)"/>
  <path d="M16 6 H170 Q170 12 176 12 V68 Q170 68 170 74 H16 Q16 68 10 68 V12 Q16 12 16 6 Z" fill="none" stroke="#d8d460" stroke-width="1"/>
</svg>
<div class="coupon-text abs">
  <strong>FREE DETAIL</strong>
  On Repairs Over $2000<br>Offer Expires: 12/31/2050<br>Offer Void With Other Offers PRINT THIS SECTION
</div>

<div class="footer-rule abs"></div>
<div class="footer-car abs" role="img" aria-label="Dark close-up of a car wheel"></div>
<div class="social abs">
  <svg width="11" height="8" viewBox="0 0 11 8" aria-label="Email"><rect width="11" height="8" fill="#fff"/><path d="M0 0 L5.5 4.5 L11 0" fill="none" stroke="#000" stroke-width="1.2"/></svg>
  <span class="ring"></span><span class="ring"></span>
</div>
<p class="footer-name abs">Tarmvale Collision</p>
<div class="footer-lines abs">
  218 Birch Ave Corvale, Texas 75990<br>
  © 2018 Tarmvale Collision- ALL RIGHTS RESERVED | ADMIN LOGIN<br>
  Privacy Policy
</div>

</body>
</html>
```